Brightwell Chilled Supplies Stationery Design

Stationery Design

Thank you to all those who have submitted the logos. We have selected the logo for our new identity and we are now looking for stationery ideas.

The attached logo must be used in all stationery designs.

We require the following items of stationery:

1. Business Cards for 10 employees – Double Sided – All the card will have the same address:

7 – 31 Marlowby Lane, Kingston Upon Thames, Surrey, KT9 3QX, United Kingdom

Office phone number: +44 (0)208 631 7094

Freephone: 0800 113 4927

Fax: +44 (0)20 8392 6481

Website: www.brightwellchilled.example

The names on the cards and mobile numbers – will be given on selection of final design.

A few of the cards will have different emails but 5/6 card will have the same email address.

2. Letterhead A4 – same contact details as above – email address to be used info@brightwellchilled.example

3. Compliments Slip – same details as no.2

4. Envelope designs – with just the address, Freephone and Website.

Sizes Required: C4 – 324mm x 229mm – Windows and Regular

DL – 110mm x 220mm – Windows and Regular

5. A4 Ring Binder – Logo at the front and back and side; company name on the front and side of the binder (Brightwell Chilled Supplies); contact details at the back; same as number 2 above.

The ring binder will have food, drink and hygiene inserts inside and will act as a temporary brochure.

It may help with the design process to know we sell a range of frozen food products including chips, burgers, fish, frozen poultry items, vegetables, ice cream, desserts, bakery products, pies, pasties, onion rings, pizza toppings etc.

We also sell ambient products such as sauces, crisps such as dunmores, chocolates such as Threlfalls, Vorreau, Pell etc.

Drinks wise we sell branded products such as zesta fizz, korvo, brisa, glint, blue heron etc; As well as juices and mineral water.

We also sell hygiene products such as tissue paper, hand towels, and other washroom products, bleaches etc.

Our website doesn’t have the full range of products but gives you a good idea of what we do www.brightwellchilled.example

Please note we are looking for a classy, slick design so don’t worry about trying to add all the products on the binder design; these have just been given to assist with the design process.

We may add a slogan to the stationery but the final decision on this still has to be taken and the profile will be updated within the next 72 hours.

This project will only last a maximum of 10-14 days, we don’t want to drag it out like the logo so please only submit creative ideas; which have been given thought in terms of design, text and graphics.

Any questions, feel free to ask.

Thank you and we look forward to your designs.

Regards

Tariq Benmore

UPDATED FILES ATTACHED

I've uploaded an Adobe Illustrator CS2.ai file, and an EPS file of my new logo so you can get better clarity within your designs for this project

Thanks
Tariq

Hi

We have had various questions in respect of dimensions and budget; we have addressed both issues below by providing dimensions and we will be increasing the budget to $500 as soon as Sketch Hive let us know how we can increase; they have already been emailed.

In respect of the dimensions, we have had various answers but here are the most common sizes.

 

There are various sizes of lever arch A4 folders but the most common ones are below:

 

 

• Dimensions width 28.5cm, height 32cm,spine 9cm
• Dimensions (mm)H:315 x W:285
• Dimensions (mm) H:31cm x W:27cm

 

The most common thickness in the UK seems to be 70mm; so can we use this as a guide please.

 

 

Compliment Slip Sizes:

 

• Our Compliment Slips are DL in size. You should design your Compliment Slip to DL dimension but also add a 3mm bleed around each edge.

 

Trim Size – 99mm x 210mm

 

With Bleed – 105mm – 216mm

 

 

Business Cards:

 

Trim Size: 85mm x 55mm

 

With Bleed: 91mm x 61mm

 

 

We have extended the time frame and the budget on this so look forward to new designs.

 

I hope this helps and all the best for Christmas and 2010..

 

Regards

Tariq Benmore.

Hi Guys

Another important point to mention as each country has different rules...

In the Uk the postage stamps go in the top right hand corner of the envelope so we will have to have our logo company details etc in either the top left or the bottom of the envelope.

Also all envelopes must have at the back our return address:

Return Address:

Brightwell Chilled Supplies Ltd
7 - 31 Marlowby Lane
Kingston Upon Thames
Surrey
KT9 3QX

So we could even have the business logo, name and website address at the front and the address at the back.

Regards

Tariq

```html
<!DOCTYPE html>
<html lang="en">
<head>
<meta charset="utf-8">
<title>Brightwell Chilled Supplies – Stationery</title>
<link href="https://fonts.googleapis.com/css2?family=Jost:wght@400;500&display=swap" rel="stylesheet">
<style>
:root{
  --navy:#252a62;
  --red:#8a1c22;
  --sky:#abd3ef;
  --ink:#1d1d22;
  --grey:#9a9a9e;
  --paper:#ffffff;
  --paper-tint:#eef3f8;
  --rule:#9fcbe6;
  --shadow:3px 3px 5px rgba(0,0,0,.35);
}
*{margin:0;padding:0;box-sizing:border-box}
html,body{width:1200px;height:1200px;overflow:hidden;background:#fff}
body{position:relative;font-family:"Jost",sans-serif;color:var(--ink)}
.piece{position:absolute;background:var(--paper);box-shadow:var(--shadow);overflow:hidden}
.swirl{position:absolute;inset:0;background:
  radial-gradient(circle at 70% 75%,var(--paper-tint) 0,rgba(238,243,248,.5) 35%,rgba(255,255,255,0) 65%),
  linear-gradient(135deg,#f4f7fb 0%,#ffffff 60%,#f3f6fa 100%)}
.brand{position:absolute;display:flex;align-items:center;gap:.35em;white-space:nowrap}
.brand .dot{width:1em;height:1em;border-radius:50%;background:var(--red);flex:none}
.brand .name{font-weight:500;color:var(--ink);line-height:1}
.small{position:absolute;color:var(--grey);line-height:1.2;white-space:nowrap}

/* ring binder */
.binder{left:5px;top:11px;width:457px;height:307px;box-shadow:var(--shadow);position:absolute}
.binder-back{position:absolute;left:0;top:0;width:223px;height:100%;background:var(--navy)}
.binder-spine{position:absolute;left:223px;top:0;width:16px;height:100%;background:var(--red)}
.binder-spine .spine-label{position:absolute;left:2px;top:2px;width:10px;height:42px;background:#fff;display:flex;align-items:center;justify-content:center}
.binder-spine .spine-label span{writing-mode:vertical-rl;font-size:3.5px;font-weight:500;color:var(--ink);white-space:nowrap}
.binder-front{position:absolute;left:235px;top:0;right:0;height:100%;background:linear-gradient(160deg,var(--sky) 0%,#b6d9f1 100%)}
.binder-front .swirl{background:radial-gradient(circle at 72% 62%,rgba(255,255,255,.25) 0,rgba(255,255,255,.08) 40%,rgba(255,255,255,0) 65%)}
.binder-back .brand{left:14px;top:284px;font-size:6px}
.binder-back .brand .name{color:#fff;white-space:normal;width:52px;line-height:1.1}
.binder-back .rule{position:absolute;left:81px;top:284px;width:1px;height:16px;background:#fff}
.binder-back .small{color:#fff;font-size:3.5px;left:86px;top:284px}

/* divider */
.divider{left:530px;top:24px;width:187px;height:285px;overflow:visible}
.divider .list{position:absolute;right:6px;top:32px;text-align:right;font-size:4px;line-height:8.1px;color:var(--grey)}
.divider .hole{position:absolute;left:8px;width:9px;height:9px;border:1px solid #555;border-radius:50%;background:#fff}
.tabs{position:absolute;left:187px;top:0;width:15px;height:117px}
.tab{position:absolute;left:0;width:15px;display:flex;align-items:center;justify-content:center}
.tab span{writing-mode:vertical-rl;font-size:3.5px;color:#fff;letter-spacing:.3px}
.tab-food{top:0;height:40px;background:var(--navy)}
.tab-drink{top:40px;height:38px;background:#5c9fd4}
.tab-hygiene{top:78px;height:39px;background:var(--red);clip-path:polygon(0 0,100% 0,100% 75%,0 100%)}

/* business cards */
.card{width:167px;height:94px}
.card-front{left:851px;top:29px}
.card-back{left:849px;top:196px}
.card-back .person{position:absolute;right:6px;top:8px;text-align:right;font-size:4.4px;line-height:1.25}
.card-back .person strong{font-weight:400;font-size:5.6px;display:block;margin-bottom:1px}

/* compliments slip */
.comp{left:69px;top:396px;width:572px;height:270px}
.comp .rule{position:absolute;left:232px;top:21px;width:1.5px;height:235px;background:var(--rule)}
.comp .title{position:absolute;left:70px;top:99px;font-size:12.5px}
.comp .details{position:absolute;left:70px;top:140px;font-size:9px;line-height:11.6px;color:var(--grey)}
.comp .details p+p{margin-top:11px}
.comp .web{position:absolute;left:70px;top:244px;font-size:9.5px;color:var(--ink)}

/* letterhead */
.letter{left:764px;top:381px;width:309px;height:425px}
.letter .rule{position:absolute;left:15px;right:12px;top:46px;height:1px;background:var(--rule)}
.letter .small{right:12px;text-align:right;font-size:4.8px}

/* envelopes */
.env-c4{left:215px;top:770px;width:235px;height:331px}
.env-dl{left:630px;top:859px;width:416px;height:208px}
.window{position:absolute;border:1px solid #333;border-radius:4px;background:#fff}
.env-c4 .window{left:72px;top:61px;width:90px;height:37px}
.env-dl .window{left:134px;top:69px;width:165px;height:70px;border-radius:7px}
.env-dl .rule{position:absolute;left:145px;top:170px;width:1px;height:28px;background:var(--rule)}
.env-dl .small{left:154px;top:172px;font-size:6.6px;line-height:9.2px}
.env-c4 .rule{position:absolute;left:83px;top:294px;width:1px;height:12px;background:var(--rule)}
</style>
</head>
<body>

<!-- A4 ring binder: back, spine, front -->
<div class="binder">
  <div class="binder-back">
    <div class="brand"><span class="dot" style="font-size:9px"></span><span class="name">Brightwell Chilled Supplies</span></div>
    <div class="rule"></div>
    <div class="small">7 – 31 Marlowby Lane, Kingston Upon Thames, Surrey, KT9 3QX, United Kingdom<br>Freephone : 0800 113 4927<br>www.brightwellchilled.example</div>
  </div>
  <div class="binder-spine"><div class="spine-label"><span>Brightwell Chilled</span></div></div>
  <div class="binder-front">
    <div class="swirl" role="img" aria-label="Soft pale swirl pattern across the binder front"></div>
    <div class="brand" style="right:12px;top:289px;font-size:7px"><span class="dot" style="font-size:9px"></span><span class="name">Brightwell Chilled Supplies</span></div>
  </div>
</div>

<!-- Food divider insert -->
<div class="piece divider">
  <div class="swirl" role="img" aria-label="Faint swirl pattern on the divider page"></div>
  <div class="brand" style="right:7px;top:11px;font-size:6px"><span class="dot" style="font-size:8px"></span><span class="name">Brightwell Chilled Supplies</span></div>
  <div class="list">chips<br>burgers<br>fish<br>frozen poultry items<br>vegetables<br>ice cream<br>desserts<br>bakery products<br>pies<br>pasties<br>onion rings<br>pizza toppings</div>
  <div class="hole" style="top:96px"></div>
  <div class="hole" style="top:168px"></div>
  <div class="tabs">
    <div class="tab tab-food"><span>FOOD</span></div>
    <div class="tab tab-drink"><span>DRINK</span></div>
    <div class="tab tab-hygiene"><span>HYGIENE</span></div>
  </div>
</div>

<!-- Business card front -->
<div class="piece card card-front">
  <div class="swirl" role="img" aria-label="Faint swirl pattern on the card front"></div>
  <div class="brand" style="left:60px;top:38px;font-size:6.5px"><span class="dot" style="font-size:12px"></span><span class="name">Brightwell Chilled Supplies</span></div>
</div>

<!-- Business card back -->
<div class="piece card card-back">
  <div class="swirl" role="img" aria-label="Faint swirl pattern on the card back"></div>
  <div class="person"><strong>First name, Last name</strong>Mobile : +44 (0) 700 000 0000<br>Email: email@brightwellchilled.example</div>
  <div class="small" style="left:6px;top:40px;font-size:4.2px">7 – 31 Marlowby Lane,<br>Kingston Upon Thames,<br>Surrey, KT9 3QX, United Kingdom</div>
  <div class="small" style="left:6px;top:62px;font-size:4.2px">Office : +44 (0)208 631 7094<br>Fax : +44 (0)20 8392 6481<br>Freephone : 0800 113 4927</div>
  <div class="small" style="left:6px;top:85px;font-size:4.2px;color:var(--ink)">www.brightwellchilled.example</div>
</div>

<!-- Compliments slip -->
<div class="piece comp">
  <div class="swirl" role="img" aria-label="Faint swirl pattern on the compliments slip"></div>
  <div class="brand" style="left:17px;top:22px"><span class="dot" style="font-size:42px;background:var(--navy)"></span><span class="name" style="font-size:15px;line-height:1.1;white-space:normal;width:120px">Brightwell Chilled Supplies</span></div>
  <div class="rule"></div>
  <div class="title">With Compliment</div>
  <div class="details">
    <p>7 – 31 Marlowby Lane,<br>Kingston Upon Thames,<br>Surrey, KT9 3QX, United Kingdom</p>
    <p>Office : +44 (0)208 631 7094<br>Fax : +44 (0)20 8392 6481<br>Freephone : 0800 113 4927<br>Email : info@brightwellchilled.example</p>
  </div>
  <div class="web">www.brightwellchilled.example</div>
</div>

<!-- Letterhead -->
<div class="piece letter">
  <div class="swirl" role="img" aria-label="Faint swirl pattern on the letterhead"></div>
  <div class="brand" style="right:12px;top:16px;font-size:8px"><span class="dot" style="font-size:16px"></span><span class="name">Brightwell Chilled Supplies</span></div>
  <div class="rule"></div>
  <div class="small" style="top:56px">7 – 31 Marlowby Lane,<br>Kingston Upon Thames,<br>Surrey, KT9 3QX, United Kingdom</div>
  <div class="small" style="top:80px">Office : +44 (0)208 631 7094<br>Fax : +44 (0)20 8392 6481<br>Freephone : 0800 113 4927<br>Email : info@brightwellchilled.example</div>
  <div class="small" style="top:111px;color:var(--ink)">www.brightwellchilled.example</div>
</div>

<!-- C4 window envelope -->
<div class="piece env-c4">
  <div class="swirl" role="img" aria-label="Faint swirl pattern on the C4 envelope"></div>
  <div class="window"></div>
  <div class="brand" style="left:15px;top:296px;font-size:5px"><span class="dot" style="font-size:10px"></span><span class="name">Brightwell Chilled</span></div>
  <div class="rule"></div>
  <div class="small" style="left:87px;top:295px;font-size:3.4px">7 – 31 Marlowby Lane, Kingston Upon Thames, Surrey, KT9 3QX, United Kingdom<br>Freephone : 0800 113 4927<br><span style="color:var(--ink)">www.brightwellchilled.example</span></div>
</div>

<!-- DL window envelope -->
<div class="piece env-dl">
  <div class="swirl" role="img" aria-label="Faint swirl pattern on the DL envelope"></div>
  <div class="window"></div>
  <div class="brand" style="left:20px;top:172px;font-size:9px"><span class="dot" style="font-size:18px"></span><span class="name" style="white-space:normal;width:95px;line-height:1.1">Brightwell Chilled Supplies</span></div>
  <div class="rule"></div>
  <div class="small">7 – 31 Marlowby Lane, Kingston Upon Thames, Surrey, KT9 3QX, United Kingdom<br>Freephone : 0800 113 4927<br><span style="color:var(--ink)">www.brightwellchilled.example</span></div>
</div>

</body>
</html>
```